Poster for teenagers

Bright, trendy, modern and young fonts - a variety of fonts, plus arrows and clip art (no photos) for an A3 size poster to be hung in study halls of schools. There are six dot points. I think each point should be in some kind of box or circle.

Here are a few ideas of the kind of thing I mean.
http://www.varrowdale.example.gov.au/Page/Images/youth_Advisory_Group_Poster_(1).jpg

http://www.brindlecourt.example/sites/default/files/Youth-Panel-Poster-1-Web.jpg

http://www.quillmarsh.example.org.au/images/librariesprovider4/Misc-illustrations/140335-qui-youth-superheros-heroup-highres.jpg?sfvrsn=0

https://pkrvworldwide.files.examplehost.com/2013/04/544477_432153653542694_970534114_n.jpg

Also my logo should be on it some where . I've attached a my logo.

Here is the text:
How to get organised and motivated this year.
1. Write stuff down
Write down things you need to do and when you plan to do them. Use digital calendars, to do apps and email lists – or pen and paper. Even if you are sure you will remember – get it out of your head and onto paper/your phone/laptop. You are more likely to get it done and feel less stressed.
2. Set up habits
If you do things in the same way, at the same time or after the same thing – then after a few weeks, it becomes much easier to get those things done. Set up a particular time, or place to do study tasks – or link them with another daily task. EG: art homework every Tuesday. Violin practice after breakfast.
3. Focus!
For 15-30 minutes at a time - totally focus on homework. Put your phone away, log out of chatterloop, close down other programs and really concentrate. Then have a break, send a text or whatever – and then go back to focussed study. Fifteen minutes of concentrated study gets more achieved than an hour of study switching back and forth between homework and other activities.
4. Just do something
No motivation? Just take a “bite”. Set a timer and just do 5 minutes. Or 15. Or read just the first two pages. Or the first problem on the worksheet. Something is better than nothing – and sometimes once you start, it’s easier to keep going.
5. Use rewards and consequences
Reward yourself when you do a hard task and use consequences when you don’t. Use food, fun activities, gaming and social time to motivate yourself – you get it when you do tasks, you don’t when you don’t. EG 15 minutes of clipstream when I finish this page. Tell other people your plans and you are more likely to stick to them.
6. Imagine the future
When you really can’t be find any motivation to do the things you need to do – take 30 seconds to think about what will happen in a week, month and year if you get on with it. What will happen then and how will that feel. And imagine what will happen in a week, month and year if you DON’T do those things – and how will that feel.

Good luck !
For free articles and one to one help with study skills, increasing motivation, coping with stress or tough times in senior school, go to tallowbrook.example.net.au
Tallow Brook Psychology and Education

```html
<!DOCTYPE html>
<html lang="en">
<head>
<meta charset="utf-8">
<title>How to get organised and motivated this year</title>
<link rel="stylesheet" href="https://fonts.googleapis.com/css2?family=Fredoka:wght@500;600&family=Patrick+Hand&family=Open+Sans:wght@400;600&display=swap">
<style>
:root{
  --sky:#3e8fd1;
  --sky-light:#6bb0e4;
  --navy:#1c3d6e;
  --mint:#dcedc4;
  --mint-edge:#b9d78f;
  --plum:#6a3c9c;
  --white:#ffffff;
  --ink:#24324a;
}
*{box-sizing:border-box;margin:0;padding:0}
html,body{width:849px;height:1200px;overflow:hidden}
body{
  position:relative;
  background:linear-gradient(135deg,var(--sky-light) 0%,var(--sky) 45%,#347fbf 100%);
  font-family:"Open Sans",sans-serif;
  color:var(--ink);
}
.title{position:absolute;left:0;top:0;width:580px;text-align:center}
.title .lead{
  display:inline-block;margin:16px 0 0;padding:4px 24px;
  background:var(--navy);color:var(--white);border-radius:30px;
  font:600 38px/1.1 "Fredoka",sans-serif;
}
.title .band{
  margin-top:10px;background:var(--white);padding:8px 20px 10px;
  border-radius:0 60px 60px 0;
  font:600 40px/1.15 "Fredoka",sans-serif;color:var(--navy);
  white-space:nowrap;
}
.title .band .soft{font:400 38px "Patrick Hand",cursive;color:var(--plum)}
.title .band .accent{color:var(--sky)}
.brand{
  position:absolute;right:14px;top:16px;width:220px;
  display:flex;align-items:center;gap:10px;
  font:600 17px/1.2 "Fredoka",sans-serif;color:var(--white);
}
.brand .dot{flex:none;width:44px;height:44px;border-radius:50%;background:var(--white)}
.figure{
  position:absolute;left:600px;top:100px;width:220px;height:270px;
  border-radius:20px;background:linear-gradient(180deg,#f3d9b8,#5b9bd3);
}
.checklist{
  position:absolute;left:560px;top:290px;width:140px;padding:8px 10px;
  background:var(--white);border:2px solid var(--navy);
  font:22px/1.3 "Patrick Hand",cursive;color:var(--navy);
}
.checklist li{list-style:none;display:flex;align-items:center;gap:6px}
.checklist svg{width:18px;height:18px;flex:none}
.tip{
  position:absolute;background:var(--mint);border:3px solid var(--mint-edge);
  border-radius:6px;padding:46px 20px 14px;
}
.tip h2{
  font:400 34px/1 "Patrick Hand",cursive;color:var(--navy);
  position:absolute;left:62px;top:-16px;
}
.tip .num{
  position:absolute;left:-4px;top:-22px;width:50px;height:50px;border-radius:50%;
  background:var(--plum);color:var(--white);
  font:600 30px/50px "Fredoka",sans-serif;text-align:center;
}
.tip p{font-size:14px;line-height:1.42;text-align:center}
.tip.t1{left:16px;top:282px;width:400px;height:240px}
.tip.t2{left:432px;top:420px;width:402px;height:215px}
.tip.t3{left:16px;top:552px;width:400px;height:240px}
.tip.t4{left:432px;top:665px;width:402px;height:190px}
.tip.t5{left:16px;top:878px;width:400px;height:240px;padding-top:76px}
.tip.t5 h2{width:300px;line-height:0.95}
.tip.t5 p{font-size:13.6px;line-height:1.38}
.tip.t6{left:432px;top:960px;width:402px;height:225px}
</style>
</head>
<body>
<header class="title">
  <div class="lead">How to get</div>
  <div class="band">ORGANISED <span class="soft">and</span> Motivated<br><span class="soft">this</span> <span class="accent">YEAR</span></div>
</header>

<div class="brand"><span class="dot"></span><span>Tallow Brook Psychology and Education</span></div>

<div class="figure" role="img" aria-label="Cartoon student holding a checklist"></div>
<ul class="checklist">
  <li><svg viewBox="0 0 18 18"><rect x="1" y="1" width="16" height="16" fill="none" stroke="#1c3d6e" stroke-width="2"/><path d="M4 9l4 4 7-9" fill="none" stroke="#6a3c9c" stroke-width="2.5"/></svg>organised</li>
  <li><svg viewBox="0 0 18 18"><rect x="1" y="1" width="16" height="16" fill="none" stroke="#1c3d6e" stroke-width="2"/><path d="M4 9l4 4 7-9" fill="none" stroke="#6a3c9c" stroke-width="2.5"/></svg>motivated</li>
</ul>

<section class="tip t1">
  <span class="num">1</span><h2>Write stuff down</h2>
  <p>Write down things you need to do and when you plan to do them. Use digital calendars, to do apps and email lists – or pen and paper. Even if you are sure you will remember – get it out of your head and onto paper/your phone/laptop. You are more likely to get it done and feel less stressed.</p>
</section>

<section class="tip t2">
  <span class="num">2</span><h2>Set up habits</h2>
  <p>If you do things in the same way, at the same time or after the same thing – then after a few weeks, it becomes much easier to get those things done. Set up a particular time, or place to do study tasks – or link them with another daily task. EG: art homework every Tuesday. Violin practice after breakfast.</p>
</section>

<section class="tip t3">
  <span class="num">3</span><h2>Focus!</h2>
  <p>For 15-30 minutes at a time - totally focus on homework. Put your phone away, log out of chatterloop, close down other programs and really concentrate. Then have a break, send a text or whatever – and then go back to focussed study. Fifteen minutes of concentrated study gets more achieved than an hour of study switching back and forth between homework and other activities.</p>
</section>

<section class="tip t4">
  <span class="num">4</span><h2>Just do something</h2>
  <p>No motivation? Just take a “bite”. Set a timer and just do 5 minutes. Or 15. Or read just the first two pages. Or the first problem on the worksheet. Something is better than nothing – and sometimes once you start, it’s easier to keep going.</p>
</section>

<section class="tip t5">
  <span class="num">5</span><h2>Use rewards and consequences</h2>
  <p>Reward yourself when you do a hard task and use consequences when you don’t. Use food, fun activities, gaming and social time to motivate yourself – you get it when you do tasks, you don’t when you don’t. EG 15 minutes of clipstream when I finish this page. Tell other people your plans and you are more likely to stick to them.</p>
</section>

<section class="tip t6">
  <span class="num">6</span><h2>Imagine the future</h2>
  <p>When you really can’t find any motivation to do the things you need to do – take 30 seconds to think about what will happen in a week, month and year if you get on with it. What will happen then and how will that feel. And imagine what will happen in a week, month and year if you DON’T do those things – and how will that feel.</p>
</section>
</body>
</html>
```